Create a new website for "The Arcade at Fernbrook"

I need a website for a shopping center in Atlanta USA. I want a classy high end look with high end motion videos (which I will provide).
The purpose of website is to attract new tenants to fill up vacant office spaces we have.
we will highlight existing cool stores and advertise that this is a cool place to start a new tenants business or office . ideally IT businesses in Alpharetta city in Georgia state in USA

Target Market(s)

commercial office tenants

Industry/Entity Type

Real Estate

Contact Information for Business Card

classy high end design
Arcade at Fernbrook
address:
2870 Briarwell Pkwy
Larkmoor FN 10482

Logo Text

I am open. Anything that attracts new IT tech tenants to lease up shopping center/ office space

Coding

Coded - Design and coding required

Number of Pages Required

5+ page

Requirements
Must have
• easy to browse

here is a link to some photos. i will provide videos shortly

http://www.tomsereph.com/2014/04/Building-Photos-3/n-5N2dg/
Nice to have
• please look at some of mall websites i like. Moving videos and images on home page

I really like this one: https://www.plazaatcresthollow.com/

others are

https://lindorecenter.com/

https://www.discoverbrisket.com/

```html
<!DOCTYPE html>
<html lang="en">
<head>
<meta charset="utf-8">
<title>The Arcade at Fernbrook</title>
<link rel="stylesheet" href="https://fonts.googleapis.com/css2?family=Poppins:wght@300;400;500;600;700&display=swap">
<style>
:root{
  --blue:#1aaee2;
  --blue-card:#22b5e9;
  --ink:#2f2f2f;
  --muted:#6a6a6a;
  --night:#1b2346;
  --tab:#eef1f1;
  --footer:#353535;
  --footer-bar:#2a2a2a;
  --white:#ffffff;
}
*{margin:0;padding:0;box-sizing:border-box}
html,body{width:1200px;height:2816px;overflow:hidden;background:var(--white)}
body{position:relative;font-family:'Poppins',sans-serif;color:var(--ink)}
.photo{position:absolute}

/* hero */
.hero{position:absolute;left:0;top:0;width:1200px;height:492px;
  background:linear-gradient(180deg,#131a3d 0%,#1e2750 40%,#4a3b2e 70%,#2a2a2e 100%)}
.brand{position:absolute;left:150px;top:48px;font-size:22px;font-weight:500;color:var(--white);letter-spacing:.3px}
.nav{position:absolute;top:54px;left:619px;display:flex;font-size:10.5px;font-weight:500;color:var(--white)}
.nav span{margin-right:31px;line-height:18px}
.nav .active{border:1.5px solid var(--white);padding:0 8px}
.hero-arrow{position:absolute;top:224px;width:37px;height:37px;background:var(--white);display:flex;align-items:center;justify-content:center}
.hero-title{position:absolute;top:322px;left:0;width:1200px;text-align:center;font-size:33px;font-weight:700;color:var(--white)}
.play{position:absolute}

/* about */
.about{position:absolute;left:0;top:492px;width:1200px;height:256px;background:var(--blue);color:var(--white)}
.about-head{position:absolute;left:140px;top:70px;width:300px;text-align:center;line-height:38px}
.about-head .light{font-size:36px;font-weight:300;display:block}
.about-head .bold{font-size:36px;font-weight:600;letter-spacing:1px;display:block}
.about-col{position:absolute;top:60px;width:262px;font-size:10.8px;line-height:16.4px;text-align:justify;font-weight:400}

/* section headings */
.sec-title{position:absolute;left:0;width:1200px;text-align:center;font-size:24px;color:var(--ink);letter-spacing:1px}
.sec-title .light{font-weight:300}
.sec-title .bold{font-weight:600}
.sec-sub{position:absolute;left:0;width:1200px;text-align:center;font-size:10.5px;line-height:16.5px;color:var(--muted)}

/* shopping grid */
.shop-intro{position:absolute;left:149px;top:952px;width:261px;height:118px;text-align:center;padding-top:14px}
.shop-intro h3{font-size:12px;font-weight:600;letter-spacing:.8px;color:var(--ink)}
.shop-intro p{font-size:10.3px;line-height:16.5px;color:var(--muted);margin-top:7px;padding:0 12px}

.projects-title{top:1640px}

/* blog */
.blog-text{position:absolute;left:188px;top:2186px;width:411px;height:244px;background:var(--blue-card);color:var(--white);padding:30px 50px 0 47px}
.blog-text h3{font-size:19px;font-weight:600;letter-spacing:.5px}
.blog-text p{font-size:10.5px;line-height:16.5px;margin-top:6px;text-align:justify}
.blog-text .date{font-size:10.5px;font-weight:600;margin-top:4px}
.share{display:flex;gap:6px;margin-top:8px}
.share i{width:10px;height:10px;border-radius:50%;background:var(--white);display:block}
.tabs{position:absolute;left:188px;top:2430px;width:824px;height:108px;display:flex}
.tab{flex:1;background:var(--tab);text-align:center;padding-top:36px;border-right:1px solid #e2e6e6}
.tab h4{font-size:13px;font-weight:600;letter-spacing:.6px;line-height:16px;color:var(--ink)}
.tab span{display:block;font-size:10.5px;color:var(--muted);margin-top:6px}
.tab.current{background:var(--blue-card);border:none}
.tab.current h4,.tab.current span{color:var(--white)}

/* footer */
.footer{position:absolute;left:0;top:2618px;width:1200px;height:159px;background:var(--footer);color:#cfcfcf}
.foot-brand{position:absolute;left:154px;top:56px;font-size:23px;font-weight:600;line-height:29px;color:var(--white)}
.foot-col{position:absolute;top:42px;font-size:10.3px;line-height:16.5px}
.foot-col h5{font-size:14px;font-weight:400;letter-spacing:.5px;color:#d8d8d8;margin-bottom:8px}
.foot-bar{position:absolute;left:0;top:2777px;width:1200px;height:39px;background:var(--footer-bar);color:#bdbdbd;font-size:10px}
.foot-bar .copy{position:absolute;left:151px;top:14px}
.foot-bar .social{position:absolute;left:1018px;top:15px;display:flex;gap:6px}
.foot-bar .social i{width:10px;height:10px;background:#9a9a9a;display:block}
</style>
</head>
<body>

<header class="hero" role="img" aria-label="Night view of the arcade building with lit storefronts and parked cars">
  <div class="brand">THE ARCADE AT FERNBROOK</div>
  <nav class="nav">
    <span class="active">HOME</span><span>ABOUT</span><span>SHOPS</span><span>OUR PROJECT</span><span>BLOG</span><span>CONTATC US</span>
  </nav>
  <div class="hero-arrow" style="left:150px"><svg width="16" height="8" viewBox="0 0 16 8"><path d="M16 4H1M4 1L1 4l3 3" fill="none" stroke="#333" stroke-width="1.2"/></svg></div>
  <div class="hero-arrow" style="left:1013px"><svg width="16" height="8" viewBox="0 0 16 8"><path d="M0 4h15M12 1l3 3-3 3" fill="none" stroke="#333" stroke-width="1.2"/></svg></div>
  <svg class="play" style="left:567px;top:234px" width="66" height="66" viewBox="0 0 66 66"><circle cx="33" cy="33" r="31" fill="none" stroke="#fff" stroke-width="2.5"/><path d="M26 20v26l21-13z" fill="none" stroke="#fff" stroke-width="2.5" stroke-linejoin="round"/></svg>
  <h1 class="hero-title">THE WORLD'S FIRST CHOICE</h1>
</header>

<section class="about">
  <h2 class="about-head"><span class="light">ABOUT</span><span class="bold">THE ARCADE AT<br>FERNBROOK</span></h2>
  <p class="about-col" style="left:481px">Lorem Ipsum is simply dummy text of the printing and typesetting industry. Lorem Ipsum has been the industry's standard dummy text ever since the 1500s, when an unknown printer took a galley of type and scrambled it to make a type specimen book. It has survived not only five centuries, but also the leap into electronic typesetting, remaining essentially unchanged.</p>
  <p class="about-col" style="left:786px">Lorem Ipsum is simply dummy text of the printing and typesetting industry. Lorem Ipsum has been the industry's standard dummy text ever since the 1500s, when an unknown printer took a galley of type and scrambled it to make a type specimen book. It has survived not only five centuries, but also the leap into electronic typesetting, remaining essentially unchanged.</p>
</section>

<h2 class="sec-title" style="top:824px"><span class="bold">SHOPPING</span></h2>
<p class="sec-sub" style="top:863px">Lorem Ipsum is simply dummy text of the printing and typesetting industry.<br>Lorem Ipsum has been the industry's standard dummy text</p>

<div class="shop-intro">
  <h3>LOREM IPSUM IS SIMPLY DUMMY</h3>
  <p>Lorem Ipsum is simply dummy text of the printing and typesetting industry. Lorem has been the industry's standard</p>
</div>
<div class="photo" style="left:149px;top:1070px;width:261px;height:170px;background:linear-gradient(180deg,#1f4a9a 0%,#3a5fa8 45%,#c89a5c 75%,#6b5a48 100%)" role="img" aria-label="Bakery storefront lit at dusk"></div>
<div class="photo" style="left:410px;top:952px;width:297px;height:288px;background:linear-gradient(180deg,#3d3d3d,#353535 60%,#2d2d2d)" role="img" aria-label="Video still of the center, dimmed"></div>
<svg class="play" style="left:536px;top:1074px" width="44" height="44" viewBox="0 0 44 44"><circle cx="22" cy="22" r="20.5" fill="none" stroke="#fff" stroke-width="1.8"/><path d="M17 13v18l14-9z" fill="none" stroke="#fff" stroke-width="1.8" stroke-linejoin="round"/></svg>
<div class="photo" style="left:707px;top:952px;width:342px;height:145px;background:linear-gradient(180deg,#4a4a4a,#3c3c3c 70%,#333)" role="img" aria-label="Video still of the clock tower, dimmed"></div>
<svg class="play" style="left:856px;top:1002px" width="46" height="46" viewBox="0 0 46 46"><circle cx="23" cy="23" r="21.5" fill="none" stroke="#fff" stroke-width="1.8"/><path d="M18 14v18l14-9z" fill="none" stroke="#fff" stroke-width="1.8" stroke-linejoin="round"/></svg>
<div class="photo" style="left:707px;top:1097px;width:342px;height:143px;background:linear-gradient(180deg,#3f7fd6 0%,#9cbce6 35%,#eef0ee 55%,#9a9a96 80%,#7a7773 100%)" role="img" aria-label="White two-storey building with parking lot"></div>

<div class="photo" style="left:0;top:1350px;width:240px;height:221px;background:linear-gradient(180deg,#e8e8e6,#f4f4f2 60%,#d8d4cc)" role="img" aria-label="White atrium with balcony railing"></div>
<div class="photo" style="left:240px;top:1350px;width:240px;height:221px;background:linear-gradient(90deg,#d9a64a,#e9c46a 40%,#f0ece4 70%,#c99e7a)" role="img" aria-label="Empty office interior with glass partition"></div>
<div class="photo" style="left:480px;top:1350px;width:242px;height:221px;background:linear-gradient(180deg,#efe8dc,#d9b980 50%,#e8dfcf)" role="img" aria-label="Stone-clad wall with elevator doors"></div>
<div class="photo" style="left:722px;top:1350px;width:242px;height:221px;background:linear-gradient(135deg,#2a66c8 0%,#6c95d4 40%,#e4e2dc 60%,#b8b4ac 100%)" role="img" aria-label="Upper walkway with railing and shadows"></div>
<div class="photo" style="left:964px;top:1350px;width:236px;height:221px;background:linear-gradient(180deg,#3d7fd8 0%,#a9c6ea 40%,#e6e4de 60%,#8f8c86 100%)" role="img" aria-label="Tower building above parking"></div>

<div class="photo" style="left:0;top:1571px;width:240px;height:220px;background:linear-gradient(180deg,#2f6fcf 0%,#8fb5e6 35%,#efefec 60%,#a49f96 100%)" role="img" aria-label="White clock tower at corner of center"></div>
<h2 class="sec-title projects-title"><span class="light">RECENT </span><span class="bold">PROJECTS</span></h2>
<p class="sec-sub" style="top:1680px">Lorem Ipsum is simply dummy text of the printing and typesetting industry.<br>Lorem Ipsum has been the industry's standard dummy text</p>
<div class="photo" style="left:964px;top:1571px;width:236px;height:220px;background:linear-gradient(180deg,#d7c3a0,#c9a872 40%,#3a342c 70%,#d6c7a8)" role="img" aria-label="Atrium stairs and railings"></div>

<div class="photo" style="left:0;top:1791px;width:240px;height:220px;background:linear-gradient(135deg,#e7e5df 0%,#2f6fcf 45%,#8a8680 75%,#c8443c 100%)" role="img" aria-label="Curved storefront row with red curb"></div>
<div class="photo" style="left:240px;top:1791px;width:240px;height:220px;background:linear-gradient(180deg,#3a7ad6 0%,#a7c3e8 35%,#eeeeea 60%,#8c8982 100%)" role="img" aria-label="Tower facade with deli storefront"></div>
<div class="photo" style="left:480px;top:1791px;width:242px;height:220px;background:linear-gradient(180deg,#8a8a86,#a73a2e 40%,#d8d6d0 60%,#8a8884 100%)" role="img" aria-label="Open interior with red steel beams"></div>
<div class="photo" style="left:722px;top:1791px;width:242px;height:220px;background:linear-gradient(180deg,#f3f5f7,#e4e6e8 40%,#bcbab4 70%,#5d5a55 100%)" role="img" aria-label="White tower above storefronts"></div>
<div class="photo" style="left:964px;top:1791px;width:236px;height:220px;background:linear-gradient(90deg,#f1efeb,#e8e4df 30%,#d7487e 70%,#c63c72)" role="img" aria-label="Vacant unit with pink walls"></div>

<h2 class="sec-title" style="top:2082px"><span class="light">RECENT </span><span class="bold">BLOG</span></h2>
<p class="sec-sub" style="top:2122px">Lorem Ipsum is simply dummy text of the printing and typesetting industry.<br>Lorem Ipsum has been the industry's standard dummy text</p>

<article class="blog-text">
  <h3>Lorem Ipsum is simply dummy</h3>
  <p>Lorem Ipsum is simply dummy text of the printing and typesetting industry. Lorem Ipsum has been the industry's standard dummy text ever since the 1500s, when an unknown printer took a galley of type and scrambled it to make a type specimen book. It has survived not only five centuries, but also the leap into electronic typesetting, remaining essentially unchanged.</p>
  <div class="date">15th January, 2020</div>
  <div class="share"><i></i><i></i></div>
</article>
<div class="photo" style="left:599px;top:2186px;width:413px;height:244px;background:linear-gradient(180deg,#34508c 0%,#6a82b0 35%,#d9a664 60%,#4c4a4c 100%)" role="img" aria-label="Storefronts at dusk with tree and parked cars"></div>

<div class="tabs">
  <div class="tab"><h4>LOREM IPSUM IS<br>SIMPLY DUMMY</h4><span>Lorem Ipsum</span></div>
  <div class="tab"><h4>LOREM IPSUM IS<br>SIMPLY DUMMY</h4><span>Lorem Ipsum</span></div>
  <div class="tab"><h4>LOREM IPSUM IS<br>SIMPLY DUMMY</h4><span>Lorem Ipsum</span></div>
  <div class="tab current"><h4>LOREM IPSUM IS<br>SIMPLY DUMMY</h4><span>Lorem Ipsum</span></div>
</div>

<footer class="footer">
  <div class="foot-brand">THE ARCADE<br>AT FERNBROOK</div>
  <div class="foot-col" style="left:377px"><h5>CONTACT</h5>T: 555.018.2741<br>F: 555.018.2741<br>info@arcadefernbrook.com</div>
  <div class="foot-col" style="left:671px"><h5>ADDRESS</h5>2870 Briarwell Pkwy<br>Larkmoor FN 10482</div>
  <div class="foot-col" style="left:910px"><h5>USER LINK</h5>PRIVACY POLICY<br>TERMS &amp; CONDITIONS<br>EARNINGS DISCLAIMER</div>
</footer>
<div class="foot-bar">
  <span class="copy">© 2019 The Arcade at Fernbrook</span>
  <span class="social"><i></i><i></i></span>
</div>

</body>
</html>
```